TidePost RV/Boat/Auto Storage

Front page for web site. Looking for a modern, clean design. Want rotating photo section (see attached) and all components similar to this web site, BUT NOT THE SAME:
https://www.marlowdepot.example/

This is a fully enclosed, for lease project. They are not condominiums for sale, or "self-storage" units. Logo and sample images are attached for your use.

Target Market(s)

Affluent customers who have high-end RV's (main focus), boats ,or automobiles.

Industry/Entity Type

Commercial real estate.

Coding

Coded - Design and coding required

Number of Pages Required

1 page

```html
<!DOCTYPE html>
<html lang="en">
<head>
<meta charset="utf-8">
<title>TidePost RV/Boat/Auto Storage</title>
<link rel="stylesheet" href="https://fonts.googleapis.com/css2?family=Oswald:wght@500;600&family=Poppins:wght@400;500;600&display=swap">
<style>
:root{
  --orange:#e2802a;
  --ink:#1f1f1f;
  --text:#3a3a3a;
  --light:#f3f3f3;
  --footer:#262626;
  --white:#ffffff;
}
*{margin:0;padding:0;box-sizing:border-box}
html,body{width:1200px;height:4988px;overflow:hidden}
body{position:relative;background:var(--white);font-family:'Poppins',sans-serif;color:var(--text)}
.abs{position:absolute}
.heading{font-family:'Oswald',sans-serif;font-weight:600;color:var(--ink);text-transform:uppercase;text-align:center;letter-spacing:.5px}
.para{font-size:17px;line-height:29px;text-align:center;color:var(--text)}
.btn{background:var(--orange);color:var(--white);border-radius:30px;font-weight:600;text-transform:uppercase;display:flex;align-items:center;justify-content:center}

/* header */
.site-header{left:0;top:0;width:1200px;height:93px;background:var(--white)}
.brand{left:84px;top:30px;font-size:27px;font-weight:600;color:var(--ink)}
.nav{left:488px;top:37px;display:flex;font-size:14px;font-weight:500;color:var(--ink)}
.nav span{margin-right:50px}
.header-cta{left:993px;top:23px;width:145px;height:49px;font-size:14px}

/* hero */
.hero{left:0;top:93px;width:1200px;height:565px;
  background:
    radial-gradient(ellipse 260px 300px at 600px 330px,rgba(190,186,170,.75),rgba(190,186,170,0) 70%),
    radial-gradient(ellipse 420px 160px at 600px 560px,rgba(150,150,140,.8),rgba(150,150,140,0) 70%),
    linear-gradient(90deg,rgba(30,40,20,.55) 0%,rgba(30,40,20,0) 25%,rgba(30,40,20,0) 75%,rgba(30,40,20,.55) 100%),
    linear-gradient(180deg,#36401f 0%,#56633a 30%,#8c9870 52%,#6d9a3c 72%,#4f7e28 100%)}
.hero-title{left:0;top:305px;width:1200px;font-size:44px;color:var(--white);font-family:'Oswald',sans-serif;font-weight:600;text-align:center;text-shadow:0 2px 6px rgba(0,0,0,.5)}
.hero-btn{left:486px;top:389px;width:228px;height:54px;font-size:15px}
.arrow{top:346px;width:56px;height:56px;border:2px solid var(--white);border-radius:50%}

/* welcome */
.welcome-title{left:0;top:765px;width:1200px;font-size:40px}
.rule{left:519px;top:850px;width:162px;height:6px;background:var(--orange)}
.welcome-text{left:190px;top:895px;width:820px}
.card{display:flex;align-items:center;justify-content:center;font-family:'Oswald',sans-serif;font-weight:600;font-size:32px;color:var(--white);text-transform:uppercase;text-shadow:0 2px 6px rgba(0,0,0,.6)}
.card-boat{left:62px;top:1180px;width:333px;height:331px;
  background:
    radial-gradient(ellipse 200px 60px at 230px 250px,rgba(225,235,240,.85),rgba(225,235,240,0) 70%),
    linear-gradient(180deg,#2c3e4c 0%,#4f6676 35%,#8ea2ad 52%,#2f6378 70%,#1e4a5e 100%)}
.card-rv{left:401px;top:1140px;width:398px;height:414px;
  background:
    radial-gradient(ellipse 140px 170px at 200px 230px,rgba(170,165,140,.8),rgba(170,165,140,0) 70%),
    linear-gradient(180deg,#3d4a2c 0%,#5d6a44 40%,#7c8a62 65%,#4f7a2e 100%)}
.card-rv::after{content:"";position:absolute;inset:12px;border:2px solid var(--white)}
.card-auto{left:807px;top:1180px;width:331px;height:331px;
  background:
    radial-gradient(ellipse 170px 70px at 160px 230px,rgba(220,222,226,.9),rgba(220,222,226,0) 70%),
    linear-gradient(180deg,#1f2731 0%,#3e4a57 35%,#7b8794 60%,#2c333c 100%)}

/* amenities */
.amenities{left:0;top:1670px;width:1200px;height:470px;
  background:
    radial-gradient(ellipse 260px 200px at 170px 240px,rgba(220,222,226,.7),rgba(220,222,226,0) 70%),
    radial-gradient(ellipse 380px 140px at 330px 430px,rgba(150,120,80,.75),rgba(150,120,80,0) 70%),
    linear-gradient(180deg,#1f2e4c 0%,#3d5277 30%,#6a7f9a 48%,#2f4a6a 60%,#3c5f7a 68%,#5d8a35 82%,#3e6424 100%)}
.amenities-title{left:0;top:1885px;width:1200px;font-family:'Oswald',sans-serif;font-weight:600;font-size:42px;color:var(--white);text-align:center;text-decoration:underline;text-underline-offset:6px;text-decoration-thickness:3px}

/* features */
.features-title{left:0;top:2200px;width:1200px;text-align:center;font-size:33px;font-weight:500;color:var(--ink)}
.features-sub{left:350px;top:2262px;width:500px;text-align:center;font-size:15px;line-height:21px;color:var(--ink)}
.features-list{left:110px;top:2378px;width:390px;list-style:none;font-size:15px;line-height:19px;color:var(--ink)}
.features-list li{display:flex;gap:10px;margin-bottom:18px}
.features-list svg{flex:0 0 17px;margin-top:1px}
.features-btn{left:110px;top:2748px;width:145px;height:47px;font-size:14px}
.features-photo{left:582px;top:2372px;width:531px;height:423px;border-radius:8px;
  background:
    radial-gradient(circle at 440px 80px,rgba(255,225,140,.95) 0,rgba(245,190,90,.5) 60px,rgba(245,190,90,0) 160px),
    radial-gradient(ellipse 260px 120px at 260px 250px,rgba(235,230,215,.85),rgba(235,230,215,0) 70%),
    linear-gradient(180deg,#3e3a22 0%,#7a6a3a 30%,#c9a766 48%,#a89a74 62%,#4e5a34 85%,#2e3a20 100%)}
.dots{left:807px;top:2812px;display:flex;gap:8px}
.dots span{width:5px;height:5px;border-radius:50%;background:#333}

/* gallery */
.gallery{left:0;top:2914px;width:1200px;height:929px;background:var(--light)}
.gallery-title{left:0;top:2990px;width:1200px;font-size:40px}
.gallery-text{left:190px;top:3070px;width:820px}
.tile{border-radius:8px}

/* location */
.location-title{left:0;top:3920px;width:1200px;font-size:40px}
.location-text{left:190px;top:4000px;width:820px}
.map{left:186px;top:4123px;width:828px;height:364px;
  background:
    radial-gradient(ellipse 110px 70px at 520px 70px,rgba(150,200,230,.9),rgba(150,200,230,0) 75%),
    radial-gradient(ellipse 160px 120px at 200px 190px,rgba(190,220,175,.9),rgba(190,220,175,0) 75%),
    radial-gradient(ellipse 200px 90px at 640px 260px,rgba(205,228,196,.9),rgba(205,228,196,0) 75%),
    linear-gradient(135deg,#e4eede 0%,#eef2ea 50%,#e2ecdc 100%)}

/* footer */
.site-footer{left:0;top:4576px;width:1200px;height:412px;background:var(--footer);color:var(--white)}
.footer-brand{left:126px;top:4632px;font-size:26px;font-weight:600;color:var(--white)}
.footer-about{left:124px;top:4693px;width:270px;font-size:13.5px;line-height:20px;color:#e6e6e6}
.social{left:126px;top:4815px;display:flex;gap:18px}
.social span{width:24px;height:24px;border-radius:50%;border:2px solid var(--white)}
.footer-head{top:4636px;font-size:18px;font-weight:600;text-transform:uppercase;color:var(--white)}
.footer-links{top:4694px;list-style:none;font-size:14px;line-height:33px;color:#e6e6e6}
.contact-row{left:861px;display:flex;gap:14px;font-size:14px;line-height:18px;color:#e6e6e6}
.contact-icon{width:40px;height:40px;border-radius:50%;background:var(--orange);display:flex;align-items:center;justify-content:center;flex:0 0 40px}
.copyright{left:0;top:4924px;width:1200px;text-align:center;font-size:14px;color:#e6e6e6}
</style>
</head>
<body>

<header class="abs site-header">
  <div class="abs brand">TidePost RV</div>
  <nav class="abs nav"><span>Home</span><span>About Us</span><span>Services</span><span>Gallery</span><span>Locations</span></nav>
  <div class="abs btn header-cta">Contact Us</div>
</header>

<section class="abs hero" role="img" aria-label="Touring motorhome driving along an oak-lined avenue"></section>
<h1 class="abs hero-title">TIDEPOST RV/BOAT/AUTO STORAGE</h1>
<div class="abs btn hero-btn">View Availabilities</div>
<svg class="abs arrow" style="left:22px" viewBox="0 0 56 56"><path d="M32 18 L22 28 L32 38" fill="none" stroke="#fff" stroke-width="3" stroke-linecap="round"/></svg>
<svg class="abs arrow" style="left:1102px" viewBox="0 0 56 56"><path d="M24 18 L34 28 L24 38" fill="none" stroke="#fff" stroke-width="3" stroke-linecap="round"/></svg>

<h2 class="abs heading welcome-title">Welcome to our website!</h2>
<div class="abs rule"></div>
<p class="abs para welcome-text">Lorem ipsum dolor sit amet, consectetur adipiscing elit, sed do eiusmod tempor incididunt ut labore et dolore magna aliqua. Quis ipsum suspendisse ultrices gravida. Risus commodo viverra maLorem ipsum dolor sit amet, consectetur adipiscing elit, sed do eiusmod tempor incididunt ut labore et dolore magna aliqua. Quis ipsum suspendisse ultrices gravida. Risus commodo viverra maecenas accumsan lacus vel facilisis. Lorem ipsum dolor sit amet, consectetur adipiscing elit, sed do eiusmod tempor incididunt ut labore et dolore magna aliquis.</p>

<div class="abs card card-boat" role="img" aria-label="White motorboat on open water under a stormy sky">Boat</div>
<div class="abs card card-rv" role="img" aria-label="Motorhome on a tree-lined road">TidePost RV</div>
<div class="abs card card-auto" role="img" aria-label="Silver sports car inside a storage hangar">Auto Storage</div>

<section class="abs amenities" role="img" aria-label="Travel trailer parked by a waterfront with picnic tables"></section>
<h2 class="abs amenities-title">AMENITIES</h2>

<h2 class="abs features-title">More than just a storage complex.</h2>
<p class="abs features-sub">Lorem ipsum dolor sit amet, consectetur adipiscinglit, sed do eiusmod tempor incididunt ut labore</p>
<ul class="abs features-list">
  <li><svg width="17" height="17" viewBox="0 0 17 17"><circle cx="8.5" cy="8.5" r="8.5" fill="#e2802a"/><path d="M4.8 8.8 L7.4 11.2 L12.2 6" fill="none" stroke="#fff" stroke-width="1.8"/></svg>Gated, secure, private, and convenient.</li>
  <li><svg width="17" height="17" viewBox="0 0 17 17"><circle cx="8.5" cy="8.5" r="8.5" fill="#e2802a"/><path d="M4.8 8.8 L7.4 11.2 L12.2 6" fill="none" stroke="#fff" stroke-width="1.8"/></svg>24' above sea level.</li>
  <li><svg width="17" height="17" viewBox="0 0 17 17"><circle cx="8.5" cy="8.5" r="8.5" fill="#e2802a"/><path d="M4.8 8.8 L7.4 11.2 L12.2 6" fill="none" stroke="#fff" stroke-width="1.8"/></svg>No leaks, flooding, or power loss during Hurricane Irma and Ian.</li>
  <li><svg width="17" height="17" viewBox="0 0 17 17"><circle cx="8.5" cy="8.5" r="8.5" fill="#e2802a"/><path d="M4.8 8.8 L7.4 11.2 L12.2 6" fill="none" stroke="#fff" stroke-width="1.8"/></svg>Security cameras.</li>
  <li><svg width="17" height="17" viewBox="0 0 17 17"><circle cx="8.5" cy="8.5" r="8.5" fill="#e2802a"/><path d="M4.8 8.8 L7.4 11.2 L12.2 6" fill="none" stroke="#fff" stroke-width="1.8"/></svg>An eight feet high perimeter fence.</li>
  <li><svg width="17" height="17" viewBox="0 0 17 17"><circle cx="8.5" cy="8.5" r="8.5" fill="#e2802a"/><path d="M4.8 8.8 L7.4 11.2 L12.2 6" fill="none" stroke="#fff" stroke-width="1.8"/></svg>65' aisles for easy maneuvering of the longest motorhome, 5th wheel, or trailered boat.</li>
  <li><svg width="17" height="17" viewBox="0 0 17 17"><circle cx="8.5" cy="8.5" r="8.5" fill="#e2802a"/><path d="M4.8 8.8 L7.4 11.2 L12.2 6" fill="none" stroke="#fff" stroke-width="1.8"/></svg>A 50 amp dedicated RV electrical outlet in each unit. Individually metered.</li>
  <li><svg width="17" height="17" viewBox="0 0 17 17"><circle cx="8.5" cy="8.5" r="8.5" fill="#e2802a"/><path d="M4.8 8.8 L7.4 11.2 L12.2 6" fill="none" stroke="#fff" stroke-width="1.8"/></svg>Multiple electric outlets and overhead lights.</li>
</ul>
<div class="abs btn features-btn">Read More</div>
<div class="abs features-photo" role="img" aria-label="Class A motorhome parked at sunset under trees"></div>
<div class="abs dots"><span></span><span></span><span></span><span></span><span></span><span></span><span></span></div>

<section class="abs gallery"></section>
<h2 class="abs heading gallery-title">Our Gallery</h2>
<p class="abs para gallery-text">Lorem ipsum dolor sit amet, consectetur adipiscing elit, sed do eiusmod tempor incididunt ut labore et dolore magna aliqua. Quis ipsum suspendisse ultrices gravida. Risus commodo viverra maLorem ipsum dolor sit amet, consectetur adipiscing elit, sed do eiusmod tempo.</p>
<div class="abs tile" style="left:72px;top:3195px;width:247px;height:195px;background:radial-gradient(ellipse 110px 50px at 150px 110px,rgba(225,225,225,.9),rgba(225,225,225,0) 70%),linear-gradient(180deg,#2e3a22 0%,#55663c 45%,#8a8f80 75%,#5a5e52 100%)" role="img" aria-label="Travel trailer parked among trees"></div>
<div class="abs tile" style="left:72px;top:3413px;width:247px;height:300px;background:radial-gradient(ellipse 110px 80px at 130px 170px,rgba(235,230,215,.85),rgba(235,230,215,0) 70%),linear-gradient(180deg,#3e3a22 0%,#b08a44 35%,#c7b48a 55%,#4b5a34 100%)" role="img" aria-label="Motorhome at sunset"></div>
<div class="abs tile" style="left:342px;top:3195px;width:248px;height:300px;background:radial-gradient(ellipse 80px 25px at 120px 115px,rgba(255,255,255,.9),rgba(255,255,255,0) 70%),linear-gradient(180deg,#c6dbe6 0%,#9cc3d6 30%,#2e86a8 50%,#1d6a8a 75%,#134f68 100%)" role="img" aria-label="Yacht cruising on blue sea"></div>
<div class="abs tile" style="left:342px;top:3518px;width:248px;height:195px;background:radial-gradient(ellipse 100px 35px at 120px 130px,rgba(235,236,238,.9),rgba(235,236,238,0) 70%),linear-gradient(180deg,#1d242d 0%,#4b5663 45%,#7c8792 65%,#2a3038 100%)" role="img" aria-label="White sports car in a hangar"></div>
<div class="abs tile" style="left:610px;top:3195px;width:247px;height:195px;background:radial-gradient(ellipse 90px 55px at 125px 100px,rgba(225,220,210,.85),rgba(225,220,210,0) 70%),linear-gradient(180deg,#44506a 0%,#9a8a7a 35%,#d8955a 60%,#7a5a38 100%)" role="img" aria-label="Class C motorhome at dusk"></div>
<div class="abs tile" style="left:610px;top:3413px;width:247px;height:300px;background:radial-gradient(ellipse 130px 35px at 170px 160px,rgba(235,240,242,.9),rgba(235,240,242,0) 70%),linear-gradient(180deg,#4d5f6c 0%,#8da0ac 40%,#3a6f86 58%,#1f4d62 100%)" role="img" aria-label="Motorboat on calm water"></div>
<div class="abs tile" style="left:880px;top:3195px;width:248px;height:300px;background:radial-gradient(ellipse 70px 60px at 190px 170px,rgba(210,30,40,.85),rgba(210,30,40,0) 75%),linear-gradient(180deg,#151515 0%,#2a2a2e 50%,#0e0e0e 100%)" role="img" aria-label="Covered sports car in a dark studio"></div>
<div class="abs tile" style="left:880px;top:3518px;width:248px;height:195px;background:radial-gradient(ellipse 110px 25px at 130px 110px,rgba(250,250,250,.9),rgba(250,250,250,0) 70%),linear-gradient(180deg,#9ea3a7 0%,#d4d7d9 45%,#e6e8e9 70%,#aeb2b5 100%)" role="img" aria-label="Aircraft inside a bright hangar"></div>

<h2 class="abs heading location-title">Location</h2>
<p class="abs para location-text">Lorem ipsum dolor sit amet, consectetur adipiscing elit, sed do eiusmod tempor incididunt ut labore et dolore magna aliqua. Quis ipsum suspendisse ultrices gravida. Risus commodo viverra maLorem ipsum dolor sit amet, consectetur adipiscing elit, sed do eiusmod tempo.</p>
<div class="abs map" role="img" aria-label="Regional road map showing the storage site"></div>
<svg class="abs" style="left:472px;top:4300px" width="58" height="58" viewBox="0 0 58 58"><circle cx="29" cy="29" r="28" fill="#fff"/><circle cx="29" cy="29" r="23" fill="#e2802a"/><path d="M29 17c-5 0-8.5 3.6-8.5 8.3 0 6 8.5 14.7 8.5 14.7s8.5-8.7 8.5-14.7C37.5 20.6 34 17 29 17z" fill="#fff"/><circle cx="29" cy="25.5" r="3" fill="#e2802a"/></svg>

<footer class="abs site-footer"></footer>
<div class="abs footer-brand">TidePost RV</div>
<p class="abs footer-about">Lorem ipsum dolor sit amet, consec tetur adipiscing elit, sed eiusmod tempor incididunt ut labore loriose dolore magna aliqua loreipsum suspendisse ultrices gravida.</p>
<div class="abs social" aria-label="Social links"><span></span><span></span><span></span></div>

<h3 class="abs footer-head" style="left:431px">Links</h3>
<ul class="abs footer-links" style="left:433px"><li>Home</li><li>About</li><li>Services</li><li>How Can Do</li><li>Contact</li></ul>
<h3 class="abs footer-head" style="left:606px">Services</h3>
<ul class="abs footer-links" style="left:607px"><li>Loisquam Service</li><li>Contrary to popular</li><li>Lorem Ipsummy</li><li>Loisquam Service</li><li>Contrary to piore</li></ul>
<h3 class="abs footer-head" style="left:861px">Contact</h3>
<div class="abs contact-row" style="top:4694px"><span class="contact-icon"><svg width="16" height="20" viewBox="0 0 16 20"><path d="M8 0C3.6 0 0.5 3.2 0.5 7.4 0.5 12.8 8 20 8 20s7.5-7.2 7.5-12.6C15.5 3.2 12.4 0 8 0z" fill="#fff"/><circle cx="8" cy="7.5" r="2.6" fill="#e2802a"/></svg></span><span>Lorem Dummyloac<br>Lor 345 Pind 338</span></div>
<div class="abs contact-row" style="top:4752px"><span class="contact-icon"><svg width="18" height="18" viewBox="0 0 24 24"><path d="M6.6 10.8a15.1 15.1 0 006.6 6.6l2.2-2.2a1 1 0 011-.25 11.4 11.4 0 003.6.57 1 1 0 011 1V20a1 1 0 01-1 1A17 17 0 013 4a1 1 0 011-1h3.5a1 1 0 011 1c0 1.25.2 2.45.57 3.57a1 1 0 01-.25 1z" fill="#fff"/></svg></span><span>Phone:<br>555 010 0147</span></div>
<div class="abs contact-row" style="top:4814px"><span class="contact-icon"><svg width="18" height="14" viewBox="0 0 18 14"><rect x="0.5" y="0.5" width="17" height="13" rx="1.5" fill="#fff"/><path d="M1 1.5 L9 8 L17 1.5" fill="none" stroke="#e2802a" stroke-width="1.5"/></svg></span><span>Email:<br>hello@tidepost.example</span></div>
<p class="abs copyright">Copyright © 2024 All rights are reserved.</p>

</body>
</html>
```